Health Coaching Flyer for New Clients

I need a two-sided flyer (3.5" x 8.5" preferred or 5" x 7") to distribute to potential coaching clients. My business name is Talvora Health & Wellness Coaching. My business is focused on helping people with habit changes that contribute to their overall well-being. I would like the design colors to be gender neutral. I would like a small photo of myself near the "my name is Jen" statement. Please feel free to change the logo color to match the design.

Target Market(s)

Adults of all ages.

Font styles to use
Serif

Requirements
Must have
• Emphasize my opening question (found in health coaching brochure - attached).
• Small picture of myself near "my name is Jen" statement.
Should not have
• No light of pastel colors.

```html
<!DOCTYPE html>
<html lang="en">
<head>
<meta charset="utf-8">
<title>Talvora Health &amp; Wellness Coaching – Flyer</title>
<link rel="stylesheet" href="https://fonts.googleapis.com/css2?family=Open+Sans:ital,wght@1,600&family=Roboto+Condensed:wght@700&family=Source+Sans+3:wght@400;600;700&display=swap">
<style>
  :root {
    --teal: #21524f;
    --charcoal: #292929;
    --white: #ffffff;
    --stage: #e8e8e8;
    --tab-gray: #c2c2c2;
    --frame-line: #d7e2e1;
    --photo-tone: linear-gradient(160deg, #8a6a5a 0%, #5a4038 55%, #3b2c28 100%);
  }
  * { box-sizing: border-box; margin: 0; padding: 0; }
  html, body { width: 948px; height: 1200px; overflow: hidden; }
  body {
    background: var(--stage);
    position: relative;
    font-family: "Source Sans 3", sans-serif;
  }
  .line { display: block; white-space: nowrap; }
  .panel {
    position: absolute;
    top: 109.5px;
    width: 418px;
    height: 1005px;
    background: var(--white);
    overflow: hidden;
  }
  .panel--front { left: 33px; }
  .panel--back { left: 499.5px; width: 416px; }
  .panel__shapes { position: absolute; inset: 0; width: 100%; height: 100%; }

  /* Front side */
  .opening-question {
    position: absolute;
    top: 62px;
    right: 70px;
    text-align: right;
    color: var(--white);
    font-family: "Open Sans", sans-serif;
    font-style: italic;
    font-weight: 600;
    font-size: 21px;
    line-height: 26.5px;
  }
  .name-tag {
    position: absolute;
    left: 125px;
    top: 208px;
    width: 38px;
    height: 212px;
    background: var(--white);
  }
  .name-tag__text {
    position: absolute;
    left: 50%;
    top: 50%;
    transform: translate(-50%, -50%) rotate(-90deg);
    white-space: nowrap;
    font-family: "Roboto Condensed", sans-serif;
    font-weight: 700;
    font-size: 27px;
    color: var(--teal);
  }
  .portrait-frame {
    position: absolute;
    left: 176px;
    top: 209px;
    width: 150px;
    height: 211px;
    border: 1.5px solid var(--frame-line);
  }
  .portrait {
    position: absolute;
    left: 10px;
    top: 10px;
    width: 128px;
    height: 189px;
    background: var(--photo-tone);
  }
  .intro {
    position: absolute;
    left: 35px;
    top: 439px;
    color: var(--white);
    font-size: 19px;
    line-height: 24px;
  }
  .intro p + p { margin-top: 24px; }
  .brand {
    position: absolute;
    left: 44px;
    top: 905px;
    color: #111;
    font-weight: 700;
  }
  .brand__name { font-size: 52px; line-height: 52px; letter-spacing: 3px; }
  .brand__tagline { font-size: 12.5px; letter-spacing: 0.4px; margin-top: 2px; }

  /* Back side */
  .benefits-title {
    position: absolute;
    left: 37px;
    top: 35px;
    width: 343px;
    height: 58px;
    background: var(--teal);
    color: var(--white);
    font-weight: 700;
    font-size: 25px;
    line-height: 58px;
    padding-left: 15px;
    white-space: nowrap;
  }
  .benefits {
    position: absolute;
    left: 31px;
    top: 104px;
    list-style: none;
    color: var(--teal);
    font-size: 19px;
    line-height: 24px;
  }
  .benefits li {
    position: relative;
    padding-left: 20px;
    margin-bottom: 6px;
  }
  .benefits li svg {
    position: absolute;
    left: 0;
    top: 4px;
    width: 15px;
    height: 15px;
  }
  .invitation {
    position: absolute;
    left: 67px;
    top: 517px;
    color: var(--white);
    font-size: 19px;
    line-height: 24px;
  }
  .invitation p + p { margin-top: 24px; }
  .contact {
    position: absolute;
    left: 70.5px;
    top: 794px;
    width: 273.5px;
    border-top: 1.5px solid var(--white);
    text-align: center;
    color: var(--white);
  }
  .contact__note { font-size: 16px; line-height: 18.5px; margin-top: 10px; }
  .contact__name { font-size: 15.5px; font-weight: 700; margin-top: 11px; line-height: 20px; }
  .contact__phone {
    margin-top: 8px;
    height: 45px;
    background: var(--white);
    color: var(--charcoal);
    font-weight: 700;
    font-size: 36px;
    line-height: 45px;
    letter-spacing: 2.5px;
  }
  .contact__email {
    margin-top: 3px;
    font-size: 16px;
    font-weight: 700;
    letter-spacing: 1.5px;
  }
</style>
</head>
<body>

<section class="panel panel--front" aria-label="Flyer front">
  <svg class="panel__shapes" viewBox="0 0 418 1005" preserveAspectRatio="none" aria-hidden="true">
    <rect x="0" y="0" width="418" height="46" fill="var(--charcoal)"/>
    <polygon points="374,0 418,0 418,463 374,453" fill="var(--charcoal)"/>
    <polygon points="0,45 374,45 374,883 0,820" fill="var(--teal)"/>
    <rect x="29" y="0" width="50.5" height="420" fill="var(--charcoal)"/>
    <rect x="29" y="0" width="50.5" height="51" fill="var(--tab-gray)"/>
    <polygon points="112,163 418,163 418,180 95,180" fill="var(--white)"/>
  </svg>

  <h1 class="opening-question">
    <span class="line">Need support in making</span>
    <span class="line">real, lasting lifestyle and</span>
    <span class="line">behavior changes?</span>
  </h1>

  <div class="name-tag"><span class="name-tag__text">My name is Jen.</span></div>
  <div class="portrait-frame">
    <div class="portrait" role="img" aria-label="Portrait photo of Jen, the health coach"></div>
  </div>

  <div class="intro">
    <p><span class="line">I am studying to become an</span><span class="line">ALIGN-Certified Functional Health</span><span class="line">Coach.</span></p>
    <p><span class="line">My training involves many</span><span class="line">science-based practices that</span><span class="line">improve both our health and how</span><span class="line">we grow and change as humans.</span></p>
    <p><span class="line">&nbsp;I now have the opportunity to turn</span><span class="line">that knowledge into practice by</span><span class="line">coaching actual clients interested in</span><span class="line">improving their own health and</span><span class="line">well-being.</span></p>
  </div>

  <div class="brand">
    <div class="brand__name">TALVORA</div>
    <div class="brand__tagline">HEALTH &amp; WELLNESS COACHING</div>
  </div>
</section>

<section class="panel panel--back" aria-label="Flyer back">
  <svg class="panel__shapes" viewBox="0 0 416 1005" preserveAspectRatio="none" aria-hidden="true">
    <polygon points="0,734 416,817 416,1005 0,1005" fill="var(--teal)"/>
    <polygon points="37,503 380,440 380,1005 37,1005" fill="var(--charcoal)"/>
  </svg>

  <h2 class="benefits-title">Functional health coaches...</h2>

  <ul class="benefits">
    <li><svg viewBox="0 0 16 16" aria-hidden="true"><polygon points="8,1 15,8 8,15 1,8" fill="none" stroke="var(--teal)" stroke-width="1.6"/></svg><span class="line">Leverage your strengths rather than</span><span class="line">focus on your weaknesses</span></li>
    <li><svg viewBox="0 0 16 16" aria-hidden="true"><polygon points="8,1 15,8 8,15 1,8" fill="none" stroke="var(--teal)" stroke-width="1.6"/></svg><span class="line">Support you in finding your own</span><span class="line">strategies and motivation for change</span></li>
    <li><svg viewBox="0 0 16 16" aria-hidden="true"><polygon points="8,1 15,8 8,15 1,8" fill="none" stroke="var(--teal)" stroke-width="1.6"/></svg><span class="line">Provide a judgment-free zone and</span><span class="line">support your autonomy</span></li>
    <li><svg viewBox="0 0 16 16" aria-hidden="true"><polygon points="8,1 15,8 8,15 1,8" fill="none" stroke="var(--teal)" stroke-width="1.6"/></svg><span class="line">Use an experimental mindset to find</span><span class="line">and develop sustainable habits</span></li>
    <li><svg viewBox="0 0 16 16" aria-hidden="true"><polygon points="8,1 15,8 8,15 1,8" fill="none" stroke="var(--teal)" stroke-width="1.6"/></svg><span class="line">Act as your accountability partner as</span><span class="line">you reach your unique health goals;</span><span class="line">whether they be improving sleep,</span><span class="line">diet, fitness, social connection, or</span><span class="line">reducing stress.</span></li>
  </ul>

  <div class="invitation">
    <p><span class="line">I would like to invite you to</span><span class="line">participate with me as a client as</span><span class="line">I continue to hone my coaching</span><span class="line">skills.&nbsp; We can develop a plan</span><span class="line">and schedule that aligns with</span><span class="line">your goals.</span></p>
    <p><span class="line">As a way to give back to my</span><span class="line">community, I am offering new</span><span class="line">clients six free coaching sessions.</span><span class="line">This is a limited time offer.</span></p>
  </div>

  <div class="contact">
    <p class="contact__note"><span class="line">Please contact me.&nbsp; I’m ready to</span><span class="line">support you as you work to improve</span><span class="line">your health.</span></p>
    <p class="contact__name">Jen Talvora</p>
    <p class="contact__phone">520-555-0147</p>
    <p class="contact__email">talvorahwc@example.com</p>
  </div>
</section>

</body>
</html>
```